Promotional business a5 Notepad design

I am looking for a custom a5 notepad design as a promotional item to give away to customers etc.
Attached will be a desk planner we had designed feel free to use as a reference.
We want the notepad to have lines running horizontal not squares like the desk planner example.

Industry/Entity Type

Hydraulic / industrial

Colors

Designer to choose colors to be used in the design.

```html
<!DOCTYPE html>
<html lang="en">
<head>
<meta charset="utf-8">
<title>Coreline Hose and Fittings – A5 Notepads</title>
<link href="https://fonts.googleapis.com/css2?family=Montserrat:wght@500;600;700&display=swap" rel="stylesheet">
<style>
  :root {
    --brand-blue: #1530c0;
    --accent-gold: #f7b500;
    --rule-grey: #9a9a9a;
    --ink: #1a1a1a;
    --paper: #ffffff;
    --backdrop: #e4e4e4;
  }
  * { margin: 0; padding: 0; box-sizing: border-box; }
  html, body { width: 1200px; height: 900px; overflow: hidden; }
  body {
    background: var(--backdrop);
    font-family: "Montserrat", Arial, sans-serif;
    position: relative;
  }
  .notepad {
    position: absolute;
    top: 106px;
    width: 484px;
    height: 686px;
    background: var(--paper);
    box-shadow: 0 2px 10px rgba(0,0,0,0.18);
    overflow: hidden;
  }
  .notepad--classic { left: 105px; }
  .notepad--wave { left: 612px; }
  .notepad svg.artwork { position: absolute; inset: 0; }
  .brand {
    position: absolute;
    display: flex;
    align-items: center;
    gap: 8px;
    font-weight: 700;
    font-size: 15px;
    letter-spacing: 0.5px;
    text-transform: uppercase;
  }
  .brand-dot { width: 30px; height: 30px; border-radius: 50%; }
  .notepad--classic .brand { left: 26px; top: 34px; color: var(--paper); }
  .notepad--classic .brand-dot { background: var(--paper); }
  .notepad--wave .brand { left: 24px; top: 30px; color: var(--brand-blue); }
  .notepad--wave .brand-dot { background: var(--brand-blue); }
  .tagline { position: absolute; color: var(--paper); font-weight: 700; }
  .notepad--classic .tagline { left: 278px; top: 26px; font-size: 16px; line-height: 21px; }
  .notepad--wave .tagline { right: 17px; top: 33px; font-size: 11px; line-height: 14px; text-align: right; }
  .label { color: var(--accent-gold); }
  .address, .email, .phone { position: absolute; white-space: nowrap; }
  .address { font-weight: 500; color: var(--ink); }
  .email { color: var(--paper); font-weight: 500; }
  .phone { color: var(--accent-gold); font-weight: 700; }

  .notepad--classic .address { left: 0; right: 0; top: 603px; text-align: center; font-size: 14px; line-height: 18px; }
  .notepad--classic .email { left: 0; right: 0; top: 636px; text-align: center; font-size: 14px; line-height: 17px; }
  .notepad--classic .phone { left: 0; right: 0; top: 653px; text-align: center; font-size: 24px; line-height: 28px; }

  .notepad--wave .address { left: 24px; top: 646px; font-size: 11px; line-height: 14px; color: var(--paper); }
  .notepad--wave .phone { right: 23px; top: 636px; font-size: 21px; line-height: 24px; }
  .notepad--wave .email { right: 23px; top: 659px; font-size: 11px; line-height: 14px; }
</style>
</head>
<body>

<section class="notepad notepad--classic" aria-label="Notepad, classic header">
  <svg class="artwork" width="484" height="686" viewBox="0 0 484 686" aria-hidden="true">
    <defs>
      <linearGradient id="steel-a" x1="0" y1="0" x2="1" y2="0">
        <stop offset="0" stop-color="#6d6d6d"/>
        <stop offset="0.5" stop-color="#c9c9c9"/>
        <stop offset="1" stop-color="#ffffff"/>
      </linearGradient>
    </defs>
    <path d="M0 0 H484 V76 C300 78 120 110 0 144 Z" fill="var(--brand-blue)"/>
    <path d="M0 156 C120 112 300 82 484 76 C300 84 120 120 0 170 Z" fill="url(#steel-a)"/>
    <g stroke="var(--rule-grey)" stroke-width="1">
      <line x1="35" y1="168" x2="450" y2="168"/>
      <line x1="35" y1="200" x2="450" y2="200"/>
      <line x1="35" y1="232" x2="450" y2="232"/>
      <line x1="35" y1="264" x2="450" y2="264"/>
      <line x1="35" y1="296" x2="450" y2="296"/>
      <line x1="35" y1="328" x2="450" y2="328"/>
      <line x1="35" y1="360" x2="450" y2="360"/>
      <line x1="35" y1="392" x2="450" y2="392"/>
      <line x1="35" y1="424" x2="450" y2="424"/>
      <line x1="35" y1="456" x2="450" y2="456"/>
      <line x1="35" y1="488" x2="450" y2="488"/>
      <line x1="35" y1="520" x2="450" y2="520"/>
      <line x1="35" y1="552" x2="450" y2="552"/>
      <line x1="35" y1="584" x2="450" y2="584"/>
    </g>
    <rect x="0" y="628" width="484" height="58" fill="var(--brand-blue)"/>
  </svg>
  <div class="brand"><span class="brand-dot"></span>Coreline</div>
  <p class="tagline">Industry Chosen Hose<br>and Fitting Provider</p>
  <p class="address"><span class="label">Address</span> 123 Fake Street, Anytown, New York 12345</p>
  <p class="email">email@corelinehose.com.au</p>
  <p class="phone">0400 315 962</p>
</section>

<section class="notepad notepad--wave" aria-label="Notepad, wave header">
  <svg class="artwork" width="484" height="686" viewBox="0 0 484 686" aria-hidden="true">
    <defs>
      <linearGradient id="steel-b" x1="0" y1="0" x2="1" y2="0">
        <stop offset="0" stop-color="#8a8a8a"/>
        <stop offset="0.45" stop-color="#e6e6e6"/>
        <stop offset="1" stop-color="#5a5a5a"/>
      </linearGradient>
      <linearGradient id="steel-c" x1="0" y1="0" x2="1" y2="0">
        <stop offset="0" stop-color="#ffffff"/>
        <stop offset="0.6" stop-color="#bdbdbd"/>
        <stop offset="1" stop-color="#6a6a6a"/>
      </linearGradient>
    </defs>
    <path d="M0 72 C70 120 170 140 250 90 C320 46 400 14 484 10 V70 C400 70 330 100 260 112 C180 130 80 135 0 134 Z" fill="url(#steel-b)"/>
    <path d="M150 134 C260 110 330 50 420 22 C450 14 470 12 484 12 V70 C410 72 330 100 260 114 C220 124 180 132 150 134 Z" fill="var(--brand-blue)"/>
    <g stroke="var(--rule-grey)" stroke-width="1">
      <line x1="35" y1="168" x2="450" y2="168"/>
      <line x1="35" y1="200" x2="450" y2="200"/>
      <line x1="35" y1="232" x2="450" y2="232"/>
      <line x1="35" y1="264" x2="450" y2="264"/>
      <line x1="35" y1="296" x2="450" y2="296"/>
      <line x1="35" y1="328" x2="450" y2="328"/>
      <line x1="35" y1="360" x2="450" y2="360"/>
      <line x1="35" y1="392" x2="450" y2="392"/>
      <line x1="35" y1="424" x2="450" y2="424"/>
      <line x1="35" y1="456" x2="450" y2="456"/>
      <line x1="35" y1="488" x2="450" y2="488"/>
      <line x1="35" y1="520" x2="450" y2="520"/>
      <line x1="35" y1="552" x2="450" y2="552"/>
      <line x1="35" y1="584" x2="307" y2="584"/>
    </g>
    <path d="M0 628 C180 624 340 600 484 548 V566 C340 612 180 630 0 632 Z" fill="url(#steel-c)"/>
    <path d="M0 634 C180 632 340 614 484 570 V686 H0 Z" fill="var(--brand-blue)"/>
  </svg>
  <div class="brand"><span class="brand-dot"></span>Coreline</div>
  <p class="tagline">Industry Chosen<br>Hoseand Fitting<br>Provider</p>
  <p class="address"><span class="label">Address</span> 123 Fake Street<br>Anytown, New York 12345</p>
  <p class="phone">0400 315 962</p>
  <p class="email">email@corelinehose.com.au</p>
</section>

</body>
</html>
```